Juniper Estates - wanted BRILLIANT website design for our new property investing company

We need a website design for our new company based in Bristol, England, UK called "Juniper Estates". We help buy people property who are in financial difficulty or who are needing to sell their property quickly for reasons such as death, divorce/separation, relocation, emigration.

We have a logo being designed incorporating strawberry and property (so red and green). We would like designs to communicate an elegant ,professional, approachable, friendly
fresh clean but also warm appealing appearance
Not too busy
Website consistent with logo and company name i.e. colour scheme

Please use our word document for content as a guide but use professional judgement for minor alterations if you feel they would benefit the site/structure etc

Please ask at any time if not sure

Target Market(s)

Adult british population, those that have a mortgage / loan / own property

Industry/Entity Type

Financial

Font styles to use
Serif
Sans Serif
Decorative

Colors
0692cd
33b7a4
acd036
fbee3e
3176b5
886aae
a6479a
e567a6
eb1f27

Requirements
Must have
• This must not look like a template website we are looking for UNIQUE please!
Nice to have
• Bristol pictures instead of generic, or colourful line drawings/comic drawings of houses/property/keys/happy people.....
Should not have
• An obvious off the shelf template design

```html
<!DOCTYPE html>
<html lang="en">
<head>
<meta charset="utf-8">
<title>Juniper Estates – The 5 easy steps</title>
<link href="https://fonts.googleapis.com/css2?family=Arimo:wght@400;700&family=Roboto+Condensed:wght@300;400;700&display=swap" rel="stylesheet">
<style>
:root{
  --red:#e8232d;
  --red-dark:#c81a22;
  --green:#8cc34a;
  --green-light:#a6d55a;
  --charcoal:#4a4a4a;
  --charcoal-dark:#3d3d3d;
  --ink:#222;
  --white:#fff;
  --grey-text:#555;
  --footer-black:#1d1d1d;
}
*{box-sizing:border-box;margin:0;padding:0}
html,body{width:1134px;height:1200px;overflow:hidden;background:var(--white)}
body{font-family:"Arimo",Arial,sans-serif;color:var(--ink)}
.page{position:relative;width:1134px;height:1200px;overflow:hidden}

/* header */
.site-header{position:absolute;left:0;top:0;width:1134px;height:124px;
  background:linear-gradient(#f4f4f4,#e9e9e9 70%,#f7f7f7)}
.brand{position:absolute;display:flex;align-items:center;gap:8px}
.brand-dot{width:22px;height:22px;border-radius:50%;background:var(--green)}
.brand-name{font-family:"Arimo",sans-serif;font-size:22px;color:var(--red);white-space:nowrap}
.site-header .brand{left:128px;top:90px}
.skyline{position:absolute;left:340px;top:58px;width:660px;height:66px;
  background:linear-gradient(90deg,#d9d9d9,#c9c9c9 30%,#e2e2e2 50%,#c9c9c9 70%,#dedede)}
.call{position:absolute;right:188px;top:18px;text-align:right;font-family:"Roboto Condensed",sans-serif}
.call-line{font-size:28px;font-weight:300;color:#777;line-height:30px}
.call-line strong{font-weight:700;color:var(--red)}
.call-mail{font-size:19px;font-weight:700;color:var(--red);line-height:26px}
.divider-v{position:absolute;left:965px;top:22px;width:1px;height:42px;background:#ccc}
.social{position:absolute;display:flex;gap:6px}
.social span{width:22px;height:22px;border-radius:50%;background:#4c8ed9;display:block}
.site-header .social{left:982px;top:31px}

/* nav */
.main-nav{position:absolute;left:0;top:124px;width:1134px;height:41px;background:var(--white);
  border-top:1px solid #ddd;display:flex;align-items:center;padding-left:105px}
.main-nav a{font-size:12.3px;color:var(--ink);text-decoration:none;padding:0 11px;height:41px;
  line-height:41px;position:relative;white-space:nowrap}
.main-nav a+a::before{content:"";position:absolute;left:0;top:14px;width:1px;height:14px;background:var(--green)}
.main-nav a:first-child{padding-left:14px;padding-right:28px}
.main-nav a:nth-child(2){padding-left:20px}
.main-nav a.active{background:#2f2f2f;color:var(--white);padding:0 13px}
.main-nav a.active::before,.main-nav a.active+a::before{display:none}

/* banner */
.banner-offer{position:absolute;left:0;top:165px;width:649px;height:103px;
  background:linear-gradient(90deg,#a3151b,#e0262e 40%,#d91f27 75%,#b9171d)}
.banner-offer p{position:absolute;left:144px;top:30px;color:var(--white);font-family:"Arimo",sans-serif;line-height:27px}
.banner-offer .thin{font-size:27px;font-weight:400;letter-spacing:-.5px;opacity:.95}
.banner-offer .bold{font-size:28px;font-weight:700;background:rgba(200,20,30,.6);padding:0 3px;margin-left:-3px}
.banner-landlords{position:absolute;left:649px;top:165px;width:485px;height:103px;
  background:linear-gradient(#ffffff,#e3f2c8 40%,#9bcf47 75%,#7cb332)}
.btn-landlords{position:absolute;left:80px;top:33px;width:199px;height:31px;border:2px solid var(--white);
  border-radius:4px;background:linear-gradient(#ee2f37,#c81a22);color:var(--white);
  font-family:"Roboto Condensed",sans-serif;font-weight:700;font-size:16px;letter-spacing:.5px;
  text-align:center;line-height:27px;box-shadow:0 1px 3px rgba(0,0,0,.3)}

/* title band */
.title-band{position:absolute;left:0;top:268px;width:1134px;height:56px;
  background:linear-gradient(#5f5f5f,#474747)}
.title-band h1{position:absolute;left:113px;top:20px;font-size:24px;font-weight:400;color:var(--white)}
.title-band::after{content:"";position:absolute;left:219px;top:56px;border:7px solid transparent;
  border-top:7px solid var(--green);border-bottom:0}

/* content */
.content{position:absolute;left:0;top:324px;width:1134px;height:649px;background:var(--charcoal)}
.steps{position:absolute;left:111px;top:32px;width:560px;color:var(--white)}
.steps h2{font-size:16px;font-weight:700;margin-bottom:20px}
.step h3{display:flex;align-items:center;gap:5px;color:var(--green);font-size:13.5px;font-weight:700;
  height:22px;margin-bottom:9px}
.step-num{width:21px;height:21px;border-radius:50%;background:var(--green);color:var(--charcoal);
  font-size:14px;font-weight:700;display:flex;align-items:center;justify-content:center}
.step ul{list-style:none;margin-bottom:14px}
.step li{position:relative;padding-left:14px;font-size:13px;line-height:17px;margin-bottom:11px;white-space:nowrap}
.step li::before{content:"";position:absolute;left:4px;top:4px;border:4px solid transparent;
  border-left:4px solid var(--green);border-right:0}

/* form */
.quick-form{position:absolute;left:649px;top:1px;width:391px;height:298px;background:var(--green);
  border-radius:0 0 14px 14px}
.quick-form h2{position:absolute;left:34px;top:30px;color:var(--white);font-family:"Arimo",sans-serif;
  font-weight:400;font-size:23px;line-height:21px;letter-spacing:-.3px}
.field{position:absolute;background:var(--white);border:1px solid #c9c9c9;border-radius:3px;
  font-size:12px;color:#666;padding:10px 0 0 13px}
.f-name{left:31px;top:82px;width:170px;height:34px}
.f-email{left:212px;top:82px;width:170px;height:34px}
.f-phone{left:31px;top:130px;width:170px;height:34px}
.f-address{left:212px;top:130px;width:170px;height:34px}
.f-message{left:31px;top:175px;width:350px;height:52px}
.btn-submit{position:absolute;left:248px;top:235px;width:118px;height:33px;border:2px solid var(--white);
  border-radius:4px;background:linear-gradient(#4a4a4a,#1e1e1e);color:var(--white);
  font-family:"Roboto Condensed",sans-serif;font-weight:700;font-size:15px;letter-spacing:1px;
  text-align:center;line-height:29px}

/* footer */
.site-footer{position:absolute;left:0;top:973px;width:1134px;height:163px;background:var(--white)}
.site-footer .brand{left:112px;top:68px}
.footer-contact{position:absolute;left:300px;top:72px;font-size:11.5px;font-weight:700;color:var(--grey-text);line-height:15px}
.footer-contact .hl{color:var(--red);font-size:14px}
.footer-contact .or{color:var(--green)}
.badge-a{position:absolute;left:790px;top:82px;width:145px;height:52px;border-radius:6px;background:#1f3a5c}
.badge-b{position:absolute;left:968px;top:54px;width:54px;height:78px;border-radius:4px;background:#2b8fc4}
.bottom-bar{position:absolute;left:0;top:1136px;width:1134px;height:64px;background:var(--footer-black)}
.footer-nav{position:absolute;left:113px;top:26px;display:flex;font-size:11px;color:var(--white)}
.footer-nav a{color:var(--white);text-decoration:none;padding:0 14px;position:relative;white-space:nowrap}
.footer-nav a:first-child{padding-left:0}
.footer-nav a+a::before{content:"|";position:absolute;left:-2px}
.bottom-bar .social{left:651px;top:20px}
.copyright{position:absolute;right:108px;top:26px;font-size:11px;color:var(--white)}
</style>
</head>
<body>
<div class="page">

  <header class="site-header">
    <div class="brand"><span class="brand-dot"></span><span class="brand-name">Juniper Estates</span></div>
    <div class="skyline" role="img" aria-label="Row of small red, green and grey houses under a cloudy sky"></div>
    <div class="call">
      <div class="call-line">call us on <strong>0117 4960382</strong></div>
      <div class="call-mail">info@juniper-estates.co.uk</div>
    </div>
    <div class="divider-v"></div>
    <div class="social"><span></span><span></span></div>
  </header>

  <nav class="main-nav">
    <a href="#">HOME</a>
    <a href="#">ABOUT US</a>
    <a href="#">SELL YOUR PROPERTY FAST</a>
    <a href="#">RENT YOUR PROPERTY FAST</a>
    <a href="#" class="active">THE 5 EASY STEPS</a>
    <a href="#">COMMON QUESTIONS</a>
    <a href="#">CONTACT US</a>
  </nav>

  <section class="banner-offer" role="img" aria-label="Red-tinted photo of a Bristol suspension bridge with hot air balloons">
    <p><span class="thin">LET US MAKE YOU</span><br><span class="bold">AN OFFER WITHIN 48 HOURS!</span></p>
  </section>
  <section class="banner-landlords" role="img" aria-label="Illustrated green meadow with houses, trees and a sunflower">
    <div class="btn-landlords">LANDLORDS CLICK HERE</div>
  </section>

  <div class="title-band"><h1>The 5 easy steps</h1></div>

  <main class="content">
    <div class="steps">
      <h2>The 5 step process:-</h2>

      <div class="step">
        <h3><span class="step-num">1</span>CONTACT US</h3>
        <ul>
          <li>Call our friendly team anytime OR fill in your contact details (on same page).</li>
          <li>We will take your details and one of our expert team will be in contact within 48hrs.<br>Usually within a very short time.</li>
        </ul>
      </div>

      <div class="step">
        <h3><span class="step-num">2</span>FREE CONSULTATION</h3>
        <ul>
          <li>This is at a suitable time for yourself in your own home. We can view the property<br>and have preliminary discussions into your problem and possible solutions.</li>
        </ul>
      </div>

      <div class="step">
        <h3><span class="step-num">3</span>GURANTEED OFFER</h3>
        <ul>
          <li>We will organize a formal CVS (Chartered Valuers Society) valuation.<br>This is to protect you and us and ensure we have an accurate valuation of your home.</li>
          <li>At this point we can give you a guaranteed offer</li>
        </ul>
      </div>

      <div class="step">
        <h3><span class="step-num">4</span>LEGAL STUFF</h3>
        <ul>
          <li>There will be paperwork to fill</li>
          <li>Solicitors from both sides (yours and ours) will ensure the deal is made into a formal contract</li>
        </ul>
      </div>

      <div class="step">
        <h3><span class="step-num">5</span>COMPLETION AND MONEY IN BANK</h3>
        <ul>
          <li>Contracts are exchanged</li>
          <li>Completion date arranged</li>
          <li>Your problems are solved!</li>
        </ul>
      </div>
    </div>

    <aside class="quick-form">
      <h2>SELL OR RENT<br>YOUR PROPERTY FAST</h2>
      <div class="field f-name">Name</div>
      <div class="field f-email">Email</div>
      <div class="field f-phone">Phone</div>
      <div class="field f-address">Property address</div>
      <div class="field f-message">Message</div>
      <div class="btn-submit">SUBMIT</div>
    </aside>
  </main>

  <footer class="site-footer">
    <div class="brand"><span class="brand-dot"></span><span class="brand-name">Juniper Estates</span></div>
    <div class="footer-contact">
      Your welcome to contact us anytime on: <span class="hl">0117 4960382</span><br>
      <span class="or">Or</span><br>
      email us at <span class="hl">info@juniper-estates.co.uk</span>
    </div>
    <div class="badge-a"></div>
    <div class="badge-b"></div>
  </footer>

  <div class="bottom-bar">
    <nav class="footer-nav">
      <a href="#">Home</a>
      <a href="#">About us</a>
      <a href="#">The 5 Easy Steps</a>
      <a href="#">Common Questions</a>
      <a href="#">Contact us</a>
      <a href="#">Sitemap</a>
    </nav>
    <div class="social"><span></span><span></span></div>
    <div class="copyright">2014 Juniper Estates Limited.Reg No 8812345</div>
  </div>

</div>
</body>
</html>
```